Artwork flyer ( named LU MO RAY ) for my music festival

I need a flyer artwork created for my indie pop, rock, hip-hop and dance music festival as soon as possible. The festival is for ages 18 to 30. Need flyer to be able to be abstracted so i can export into different social media
sizes etc

Here is some information around the music festival details.

Title: LU MO RAY ( music festival)

Artists :
KIRO Fen
Mirela Post
TRGs
The Brindles
Zank Pods
Velvet Otter
Copper ah
Quiet Tundra

Venue: Harrowmere Paddock Club
Date: Saturday 25th March
Tickets: www.tikvarro.com.au

Logo Text

LUMO RAY ( or LU MO RAY)

```html
<!DOCTYPE html>
<html lang="en">
<head>
<meta charset="utf-8">
<title>LUMO RAY Music Festival</title>
<link rel="stylesheet" href="https://fonts.googleapis.com/css2?family=Alfa+Slab+One&family=Bowlby+One&family=Baloo+2:wght@800&family=Fredoka:wght@600&family=Bungee&family=Staatliches&family=Oswald:wght@400&display=swap">
<style>
  :root {
    --paper: #c9a26c;
    --band-text: #ecd6a8;
    --title-face: #b97a3a;
    --title-side: #8d8a2c;
    --white: #f4f4f2;
    --white-side: #9aa3a6;
    --red: #d7463b;
    --red-side: #9e2b22;
    --yellow: #f2bf2e;
    --yellow-side: #a9781a;
    --blue: #3f8fd6;
    --blue-side: #245d93;
    --green: #4dba2c;
    --green-side: #2a7416;
    --orange: #d9602d;
    --orange-side: #8f3a17;
    --sky: #57b8ef;
    --sugar: #c98a3c;
    --sugar-side: #7a4f1d;
  }
  html, body { margin: 0; padding: 0; overflow: hidden; }
  body { width: 938px; height: 1200px; background: var(--paper); }
  .poster { position: relative; width: 938px; height: 1200px; overflow: hidden; background: var(--paper); }
  .poster-art { position: absolute; inset: 0; }
  .line { position: absolute; left: 0; width: 938px; text-align: center; white-space: nowrap; margin: 0; }
  .title {
    top: 112px; font-family: "Bowlby One", sans-serif; font-size: 112px; line-height: 1;
    color: var(--title-face); letter-spacing: 1px;
    text-shadow: 1px 2px 0 var(--title-side), 2px 4px 0 var(--title-side), 3px 6px 0 var(--title-side), 4px 8px 0 var(--title-side), 5px 10px 0 var(--title-side), 6px 14px 12px rgba(40,25,10,.5);
  }
  .subtitle {
    top: 270px; font-family: "Alfa Slab One", serif; font-size: 40px; line-height: 1;
    color: var(--band-text); letter-spacing: 7px;
    text-shadow: 2px 2px 2px rgba(50,30,10,.45);
  }
  .act { position: absolute; white-space: nowrap; margin: 0; line-height: 1; }
  .act-kiro { left: 196px; top: 346px; font-family: "Baloo 2", sans-serif; font-size: 66px; color: var(--white);
    text-shadow: 1px 2px 0 var(--white-side), 2px 4px 0 var(--white-side), 3px 6px 0 var(--white-side), 4px 10px 8px rgba(0,0,0,.45); }
  .plaque { position: absolute; display: flex; align-items: center; justify-content: center; border-radius: 4px; }
  .plaque-mirela { left: 472px; top: 432px; width: 282px; height: 84px; background: var(--red);
    box-shadow: 0 8px 0 var(--red-side), 0 14px 16px rgba(0,0,0,.4); border-radius: 10px; }
  .plaque-mirela .act { position: static; font-family: "Fredoka", sans-serif; font-size: 38px; color: var(--yellow); }
  .act-trgs { left: 196px; top: 482px; font-family: "Alfa Slab One", serif; font-size: 72px; color: var(--yellow);
    text-shadow: 1px 2px 0 var(--yellow-side), 2px 4px 0 var(--yellow-side), 3px 6px 0 var(--yellow-side), 4px 10px 8px rgba(0,0,0,.4); }
  .plaque-brindles { left: 404px; top: 572px; width: 296px; height: 90px; background: var(--blue);
    box-shadow: 0 8px 0 var(--blue-side), 0 14px 16px rgba(0,0,0,.4); }
  .plaque-brindles .act { position: static; font-family: "Alfa Slab One", serif; font-size: 31px; color: var(--yellow);
    text-shadow: 1px 2px 0 var(--yellow-side); }
  .act-zank { left: 336px; top: 684px; font-family: "Bungee", sans-serif; font-size: 63px; color: var(--green);
    text-shadow: 1px 2px 0 var(--green-side), 2px 4px 0 var(--green-side), 3px 6px 0 var(--green-side), 4px 10px 8px rgba(0,0,0,.4); }
  .act-velvet { left: 196px; top: 786px; font-family: "Staatliches", sans-serif; font-size: 80px; color: var(--orange); letter-spacing: 2px;
    text-shadow: 1px 2px 0 var(--orange-side), 2px 4px 0 var(--orange-side), 3px 6px 0 var(--orange-side), 4px 10px 8px rgba(0,0,0,.4); }
  .plaque-copper { left: 432px; top: 868px; width: 252px; height: 92px; background: var(--red);
    box-shadow: 0 8px 0 var(--red-side), 0 14px 16px rgba(0,0,0,.4); }
  .plaque-copper .act { position: static; font-family: "Bungee", sans-serif; font-size: 30px; color: var(--sky); transform: skewX(-12deg); }
  .act-tundra { left: 0; width: 938px; text-align: center; top: 990px; font-family: "Alfa Slab One", serif; font-size: 60px; color: var(--sugar); letter-spacing: 4px;
    text-shadow: 1px 2px 0 var(--sugar-side), 2px 4px 0 var(--sugar-side), 3px 6px 0 var(--sugar-side), 4px 10px 8px rgba(0,0,0,.45); }
  .details { top: 1096px; font-family: "Oswald", sans-serif; font-size: 38px; color: var(--band-text); word-spacing: 2px;
    text-shadow: 1px 2px 2px rgba(40,25,10,.5); }
  .details .gap { display: inline-block; width: 34px; }
  .tickets { top: 1158px; font-family: "Alfa Slab One", serif; font-size: 27px; color: var(--band-text); letter-spacing: 5px;
    text-shadow: 1px 2px 2px rgba(40,25,10,.45); }
</style>
</head>
<body>
<main class="poster">
  <svg class="poster-art" width="938" height="1200" viewBox="0 0 938 1200">
    <defs>
      <linearGradient id="panelFill" x1="0" y1="0" x2="1" y2="1">
        <stop offset="0" stop-color="#5c4229"/>
        <stop offset="0.5" stop-color="#7d5e3e"/>
        <stop offset="1" stop-color="#5e4329"/>
      </linearGradient>
      <linearGradient id="bandFill" x1="0" y1="0" x2="0" y2="1">
        <stop offset="0" stop-color="#9c774d"/>
        <stop offset="1" stop-color="#7f5f3d"/>
      </linearGradient>
    </defs>
    <rect class="paper" width="938" height="1200" fill="var(--paper)"/>
    <rect class="centre-panel" x="76" y="44" width="786" height="1050" rx="18" fill="url(#panelFill)" stroke="#4b331d" stroke-opacity=".5" stroke-width="3" role="img" aria-label="Textured backdrop with scattered colourful leaves"/>
    <rect class="title-band" x="0" y="262" width="938" height="56" fill="url(#bandFill)"/>
    <rect x="0" y="316" width="938" height="4" fill="#5a3f25" opacity=".5"/>
    <rect class="footer-band" x="0" y="1080" width="938" height="120" fill="url(#bandFill)"/>
    <rect x="0" y="1080" width="938" height="3" fill="#5a3f25" opacity=".5"/>
  </svg>

  <h1 class="line title">LUMO RAY</h1>
  <p class="line subtitle">MUSIC FESTIVAL</p>

  <p class="act act-kiro">KIRO Fen</p>
  <div class="plaque plaque-mirela"><p class="act">Mirela Post</p></div>
  <p class="act act-trgs">TRGs</p>
  <div class="plaque plaque-brindles"><p class="act">THE BRINDLES</p></div>
  <p class="act act-zank">ZANK PODS</p>
  <p class="act act-velvet">VELVET OTTER</p>
  <div class="plaque plaque-copper"><p class="act">COPPER AH</p></div>
  <p class="act act-tundra">QUIET TUNDRA</p>

  <p class="line details">HARROWMERE PADDOCK CLUB<span class="gap"></span>SATURDAY 25TH MARCH</p>
  <p class="line tickets">TICKETS: WWW.TIKVARRO.COM.AU</p>
</main>
</body>
</html>
```